Immobilienfirma sucht Flyerdesign
Zielgruppe
Wir sind ein Immobilienmaklerbüro spezialisiert auf den Verkauf von Einfamilienhäusern und Baugrundstücken im Umland von Berlin (Havelland & Oberhavel).
Zielgruppe des Flyers sind ausschließlich Eigentümer von Immobilien die verkaufen möchten.
Wir benötigen 6 - 8 Mal pro Jahre neue Flyer. Wir haben daher Interesse an einer regelmäßigen Zusammenarbeit.
Aufgabenstellung
Der Flyer soll im Format A 4 sein (hochkant).
Es soll eher Text sprechen, da wir möglichst viel Informationen transportieren möchten.
Wir richten uns ausschließlich an die Eigentümer (Verkäufer) von Immobilie die wir begeistern möchten gerade über uns zu verkaufen.
Unser Alleinstellungsmerkmal ist als "Makler OHNE Schilder" zu arbeiten, im Gegensatz zu unseren Mitbewerbern die die ganze Stadt zuplakatieren mit Werbebannern an Gartenzäunen und Straßenecken, Maklerschildern und Maklergalgen vor den zum Verkauf stehen Häusern etc.
Wir verkaufen diskret und bieten Verkäufern ein Komplettpaket von der unverbindlichen Erstberatung, über die kostenlose Wertermittlung, den kostenlosen Energieausweis, den kompletten Verkauf (natürlich ohne Schilder) bis zum Notartermin. Auch danach sind wir für den Verkäufer da und suchen ihm eine neue Bleibe und helfen auch mit Umzugsfirmen etc.
Komplettprogramm für Verkäufer - und selbstverständlich für Verkäufer komplett KOSTENLOS !
Als Bilder dachten wir an ein Portraitfoto von mir das mit Angebot ein Gesicht bekommt und der Kunde weiß wer ihm gegenüber sitzt, sowie ein eycatcher Bild.
Wir bieten unseren Kunden einen diskreten und schnellen Verkauf. Komplettservice : Kostenlose Wertermittlung, kostenloser Energieausweis, Übernahme des kompletten Verkaufs bis zum Notartermin, Hilfe bei der Suche nach neuer Immobilie, Hilfe beim Umzug.

```html
<!DOCTYPE html>
<html lang="de">
<head>
<meta charset="utf-8">
<title>Immobilienkontor Brenneke – Flyer</title>
<link href="https://fonts.googleapis.com/css2?family=Open+Sans:wdth,wght@75..100,400..800&family=Saira:wght@300&family=Saira+Semi+Condensed:wght@800&display=swap" rel="stylesheet">
<style>
  :root {
    --green: #6e8a67;
    --grey: #c4c6c4;
    --grey-light: #d9dbd9;
    --page-bg: #e4e4e4;
    --ink: #232323;
    --white: #ffffff;
  }
  * { box-sizing: border-box; margin: 0; padding: 0; }
  html, body { width: 1200px; height: 1200px; overflow: hidden; background: var(--page-bg); }
  body { font-family: "Open Sans", Arial, sans-serif; font-stretch: 75%; color: var(--ink); }

  .flyer {
    position: absolute; left: 197px; top: 20px;
    width: 806px; height: 1160px;
    background: var(--white);
    box-shadow: 0 4px 18px rgba(0,0,0,.18);
    overflow: hidden;
  }

  .header-band { position: absolute; left: 0; top: 0; width: 100%; height: 122px; background: var(--grey); }
  .company-title {
    position: absolute; left: 68px; top: 62px;
    font-family: "Saira", Arial, sans-serif; font-weight: 300;
    font-size: 31px; color: var(--white); letter-spacing: .2px;
  }
  .header-rule { position: absolute; left: 0; top: 130px; width: 100%; height: 3px; background: var(--grey-light); }

  .discreet-tag { position: absolute; right: 0; top: 0; width: 260px; height: 200px; }
  .discreet-text {
    position: absolute; right: 22px; top: 32px; width: 170px;
    text-align: center; color: var(--white); transform: rotate(6deg);
  }
  .discreet-text .tag-main { font-weight: 800; font-size: 19px; line-height: 1.05; font-stretch: 85%; }
  .discreet-text .tag-note { font-size: 9px; line-height: 1.25; margin-top: 3px; font-weight: 600; }

  .hero-photo {
    position: absolute; left: 0; top: 136px; width: 100%; height: 416px;
    background: linear-gradient(180deg, #a8b3cc 0%, #c2c3d3 30%, #b8ae9f 62%, #6f7450 82%, #4d6a34 100%);
  }

  .content-panel { position: absolute; left: 40px; top: 552px; right: 8px; bottom: 90px; background: var(--white); }
  .headline {
    position: absolute; left: 36px; top: 14px; white-space: nowrap;
    font-family: "Saira Semi Condensed", Arial, sans-serif; font-weight: 800;
    font-size: 46px; line-height: 1; color: var(--green);
  }
  .intro-columns {
    position: absolute; left: 36px; top: 80px; width: 690px;
    column-count: 3; column-gap: 24px;
    font-size: 11px; line-height: 16px;
  }
  .intro-columns p { margin-bottom: 14px; }

  .service-heading {
    position: absolute; left: 36px; top: 372px; width: 500px;
    font-family: "Saira Semi Condensed", Arial, sans-serif;
    font-weight: 800; font-size: 18px; line-height: 23px; color: var(--green);
  }
  .service-list {
    position: absolute; left: 56px; top: 424px; width: 480px;
    list-style: none; font-weight: 700; font-size: 14px; line-height: 19px; font-stretch: 80%;
  }
  .service-list li { position: relative; white-space: nowrap; }
  .service-list li::before {
    content: ""; position: absolute; left: -14px; top: 8px;
    width: 5px; height: 5px; border-radius: 50%; background: var(--green);
  }

  .footer-url {
    position: absolute; left: 20px; top: 1060px; width: 250px; height: 72px;
    background: var(--green); color: var(--white);
    font-size: 14px; font-weight: 700; font-stretch: 85%;
    display: flex; align-items: flex-end; padding: 0 0 12px 16px;
  }
  .footer-contact {
    position: absolute; left: 270px; top: 1060px; width: 310px; height: 72px;
    background: var(--grey-light); padding: 8px 12px; font-size: 10px; line-height: 14px;
  }
  .footer-contact .contact-name { font-size: 14px; font-weight: 700; line-height: 20px; margin-top: 4px; }

  .portrait {
    position: absolute; left: 580px; top: 900px; width: 226px; height: 232px;
    background: linear-gradient(180deg, #eef0f0 0%, #d8d4cf 45%, #2c3340 75%, #1e2530 100%);
  }
</style>
</head>
<body>
  <main class="flyer">
    <div class="header-band"></div>
    <h1 class="company-title">Immobilienkontor Brenneke</h1>
    <div class="header-rule"></div>

    <div class="hero-photo" role="img" aria-label="Foto eines beleuchteten Einfamilienhauses mit Doppelgarage in der Abenddämmerung"></div>

    <svg class="discreet-tag" viewBox="0 0 260 200" aria-hidden="true">
      <path d="M8 22 L260 26 L260 130 L130 130 C110 120 112 80 70 70 C40 62 20 48 8 22 Z" fill="var(--green)"/>
      <path d="M8 22 C20 48 40 62 70 70 C112 80 110 120 130 130 C95 150 82 185 84 195 C70 150 40 130 30 100 C20 70 12 44 8 22 Z" fill="#eef0ee"/>
      <path d="M8 22 C20 48 40 62 70 70 C112 80 110 120 130 130" fill="none" stroke="#b9bdb9" stroke-width="1.2"/>
    </svg>
    <div class="discreet-text">
      <div class="tag-main">VERKAUF<br>100% DISKRET</div>
      <div class="tag-note">(grundsätzlich KEINE Verkaufsschilder auf Ihrem Grundstück!)</div>
    </div>

    <section class="content-panel">
      <h2 class="headline">Wir verkaufen Ihre Immobilie!</h2>
      <div class="intro-columns">
        <p>Die Firma Immobilienkontor Brenneke aus Falkensee ist spezialisiert auf den Verkauf von Immobilien im Havelland. Wir verkaufen diskret, schnell und professionell Immobilien aller Art in der Stadt Falkensee, sowie der Gemeinde Dallgow-Döberitz, Schönwalde-Glien, Brieselang.</p>
        <p>Auch das Gebiet Oberhavel mit den Städten Hohen Neuendorf, Hennigsdorf, Oranienburg und Birkenwerder gehören zu unserem Tätigkeitsgebiet. Letztlich sind die Städte Berlin und Potsdam sowie Umgebung wie Groß Glienicke, Seeburg und Ketzin unser Aktionsgebiet.</p>
        <p>Unsere Firma verkauft Einfamilienhäuser, Zweifamilienhäuser, Villen und Mehrfamilienhäuser. Zu unserem Verkaufsangebot gehören zudem Baugrundstücke und Neubauprojekte. Auch Eigentumswohnungen und Kapitalanlagen werden seit Jahren erfolgreich von unserer Firma Immobilienkontor Brenneke verkauft. Letztlich verkaufen wir auch Gewerbeimmobilien von der Gewerbehalle über Hotels und Pensionen bis zum Bauernhof.</p>
        <p>Als der Makler ohne Schilder ist unsere Firma Immobilienkontor Brenneke in Falkensee und Umgebung tätig. Wir heben uns hiermit von anderen Maklerfirmen deutlich ab, da wir komplett ohne Schilder arbeiten. Wir verkaufen Immobilien in Falkensee und dem Umland also sehr diskret.</p>
        <p>Gerade Immobilien in Falkensee erfreuen sich sehr starker Beliebtheit, da diese Immobilien sehr dicht an Berlin-Spandau gelegen sind und eine erstklassige Infrastruktur bieten. Zudem bietet Falkensee einen Regioanschluss nach Berlin. Immobilien in Schönwalde bieten ein sehr grünes Wohnen mit Waldcharakter. Immobilien in Hohen Neuendorf wiederum bieten direkte Nähe von Berlin-Reinickendorf und ebenfalls eine optimale Infrastruktur.</p>
        <p>Wir sind Immobilienmakler seit über 20 Jahren und bieten unseren Kunden daher hunderte Referenzen. Immobilienkontor Brenneke – Ihr Immobilienpartner für Falkensee sowie das Havelland und Oberhavel sowie Berlin.</p>
      </div>

      <h3 class="service-heading">Wir bieten Ihnen den kompletten Service aus<br>einer Hand und für Sie als Eigentümer völlig kostenlos!</h3>
      <ul class="service-list">
        <li>Kostenfreie &amp; unverbindliche Wertermittlung Ihrer Immobilie</li>
        <li>Kostenloser Energieausweis der für den Verkauf gesetzlich vorgeschrieben ist</li>
        <li>Kostenlose Einholung aller Genehmigungen etc.</li>
        <li>Keine Verkäuferprovisionen!</li>
      </ul>
    </section>

    <div class="portrait" role="img" aria-label="Porträtfoto des Maklers im dunklen Anzug mit roter Krawatte"></div>

    <div class="footer-url">www.immobilien-havelblick.biz</div>
    <div class="footer-contact">
      <div>Wir sind jederzeit für Sie erreichbar:</div>
      <div class="contact-name">Matthias Brenneke · Tel. 03322 5501846</div>
      <div>Fax: 03212 2208451 · Mail: raumkontorwest@havelpost.eu</div>
    </div>
  </main>
</body>
</html>
```